Engineering and Energy service provider

We need a design that gives the impression of a high level of technical competence and a reliable partner. Simple structure with little need for updates.
The company brand is Valomir and today consists of two main businesses: energy optimisation (Valomir energy) and technical consultancy (Valomir Engineering). Valomir energy is shown in the attached powerpoint,
We are a young growing company that consists of several businesses, the largest parts are energy monitoring services and consulting services. Consulting services for commercial installations in the technical area of cooling, ventilation, heating and energy. Services offered include project planning, project management, inspection, operational analysis and technical investigations. Energy monitoring and optimization services are performed as a subscription with a subscription to the service.
Updates
Bug in system deadline before launch
Target Market(s)
Commercial property owners Grocery retail, grocery stores, construction companies
Industry/Entity Type
energy services and consulting services
Coding
Coded - Design and coding required
Number of Pages Required
5+ page
Look and feel
Each slider illustrates characteristics of the customer's brand and the style your logo design should communicate.

```html
<!DOCTYPE html>
<html lang="en">
<head>
<meta charset="UTF-8">
<title>Valomir Engineering</title>
<link href="https://fonts.googleapis.com/css2?family=Michroma&family=Poppins:wght@400;500;600;700&display=swap" rel="stylesheet">
<style>
:root{
  --orange:#f39a1e;
  --orange-deep:#ee7a22;
  --yellow:#f8c02a;
  --blue:#1f5fb8;
  --ink:#1b1b1b;
  --muted:#5a5f66;
  --line:#d9dde2;
  --grey-bg:#f1f2f4;
  --white:#ffffff;
  --black:#000000;
}
*{box-sizing:border-box;margin:0;padding:0}
html,body{width:1200px;height:4012px;overflow:hidden}
body{font-family:"Poppins",sans-serif;color:var(--ink);background:var(--white);position:relative}
.display{font-family:"Michroma",sans-serif;letter-spacing:5px;text-transform:uppercase;font-weight:400}
section,footer{position:relative;width:1200px;overflow:hidden}

/* header + hero */
.hero{height:660px;background:linear-gradient(120deg,#1c2533 0%,#2e3a4a 45%,#3d3a33 70%,#1a1f28 100%);border-bottom:6px solid var(--orange)}
.hero-photo{position:absolute;inset:0;background:radial-gradient(ellipse at 25% 45%,rgba(214,150,80,.35),transparent 55%),radial-gradient(ellipse at 80% 40%,rgba(80,130,190,.35),transparent 55%)}
.hero-shade{position:absolute;inset:0;background:linear-gradient(180deg,rgba(0,0,0,.55) 0%,rgba(0,0,0,.35) 50%,rgba(0,0,0,.6) 100%)}
.nav{position:absolute;top:30px;left:140px;right:140px;display:flex;align-items:center;justify-content:space-between;z-index:2}
.brand{font-family:"Poppins",sans-serif;font-weight:700;font-size:26px;letter-spacing:4px;color:var(--white)}
.menu{display:flex;gap:26px;align-items:center}
.menu a{color:var(--white);text-decoration:none;font-size:13px;font-weight:500}
.menu a.active{color:var(--orange)}
.menu a.btn{color:var(--black)}
.btn{display:inline-block;font-size:12px;font-weight:600;padding:11px 20px;text-decoration:none;border-radius:2px}
.btn-orange{background:var(--orange);color:var(--black)}
.btn-blue{background:var(--blue);color:var(--white)}
.hero-copy{position:absolute;top:245px;left:0;right:0;text-align:center;z-index:2}
.hero-copy h1{font-size:36px;line-height:1.4;color:var(--white)}
.hero-copy h1 span{color:var(--orange)}
.hero-copy p{color:#e8e8e8;font-size:15px;max-width:600px;margin:16px auto 0;line-height:1.55}
.hero-actions{margin-top:30px;display:flex;gap:16px;justify-content:center}
.seal{position:absolute;left:578px;width:44px;height:44px;border-radius:50%;background:var(--white);border:4px solid var(--orange);z-index:3}
.seal::after{content:"";position:absolute;inset:8px;border-radius:50%;background:var(--blue)}

/* expertise */
.expertise{height:660px;text-align:center;padding-top:110px}
.expertise h2{font-size:32px;line-height:1.45}
.sub{font-size:14px;color:var(--muted);margin-top:28px}
.systems{display:flex;gap:22px;justify-content:center;margin-top:64px}
.system-card{width:230px;height:200px;border:1px solid var(--line);display:flex;flex-direction:column;align-items:center;justify-content:center;gap:18px;font-size:15px;line-height:1.4}
.system-card svg{width:48px;height:48px}

/* services */
.services{height:560px;background:var(--grey-bg)}
.services-photo{position:absolute;left:0;top:88px;width:560px;height:412px;background:linear-gradient(135deg,#3a4450,#6b6e70 45%,#b5482f 60%,#2f3a46)}
.services-copy{position:absolute;left:610px;top:150px}
.services-copy h2{font-size:30px;line-height:1.45}
.service-list{list-style:none;margin-top:30px}
.service-list li{display:flex;align-items:center;gap:18px;font-size:15px;margin-bottom:14px}
.service-list li::before{content:"";width:10px;height:10px;background:var(--orange);transform:rotate(45deg)}

/* band */
.band{height:460px;background:linear-gradient(90deg,var(--orange-deep),var(--yellow));text-align:center;padding-top:150px}
.band h2{font-size:32px;line-height:1.5;color:var(--ink)}
.band p{font-size:14px;max-width:700px;margin:22px auto 0;line-height:1.6}
.band .btn{margin-top:28px}

/* process */
.process{height:660px;text-align:center;padding-top:80px}
.process h2{font-size:32px;line-height:1.45}
.steps{display:flex;justify-content:center;gap:60px;margin-top:56px}
.step{width:180px}
.step svg{width:180px;height:180px}
.step h3{font-size:17px;font-weight:500;margin-top:22px}
.step p{font-size:13px;color:var(--muted);line-height:1.5;margin-top:6px}

/* cases */
.cases{height:620px;text-align:center;padding-top:60px;background:linear-gradient(180deg,#fff 0%,#f4f6f9 100%)}
.cases h2{font-size:32px}
.case-row{display:flex;gap:28px;justify-content:center;margin-top:56px}
.case{width:300px;text-align:left}
.case-photo{height:200px;background:linear-gradient(160deg,#5d7fa8,#1f3656)}
.case:nth-child(2) .case-photo{background:linear-gradient(160deg,#7b8a99,#2c3948)}
.case:nth-child(3) .case-photo{background:linear-gradient(160deg,#9fb6cf,#26476e)}
.case h3{font-size:16px;font-weight:500;margin-top:20px;white-space:nowrap}
.case p{font-size:12px;color:var(--muted);line-height:1.5;margin-top:8px}
.case a{display:block;margin-top:14px;font-size:12px;font-weight:600;color:var(--ink);text-decoration:none}
.arrow{position:absolute;top:330px;font-size:30px;color:var(--ink)}

/* footer */
.footer{height:392px;background:var(--black);color:var(--white);border-top:6px solid var(--orange)}
.footer .brand{position:absolute;left:140px;top:78px}
.footer-menu{position:absolute;right:140px;top:86px;display:flex;gap:24px}
.footer-menu a{color:var(--white);font-size:12px;font-weight:500;text-decoration:none}
.footer-rule{position:absolute;left:140px;right:140px;top:150px;border-top:1px solid #333}
.contact{position:absolute;top:182px;font-size:14px;line-height:1.6}
.contact h4{color:var(--orange);font-size:13px;font-weight:600}
.cert{position:absolute;right:140px;top:186px;width:56px;height:56px;background:var(--white);border-radius:4px}
.copyright{position:absolute;left:0;right:0;top:318px;text-align:center;font-size:12px}
</style>
</head>
<body>

<section class="hero">
  <div class="hero-photo" role="img" aria-label="Engineer working at an industrial control panel"></div>
  <div class="hero-shade"></div>
  <nav class="nav">
    <div class="brand">VALOMIR</div>
    <div class="menu">
      <a href="#">HOME</a><a href="#">ABOUT US</a><a href="#">SERVICES</a><a href="#">VALOMIR ENERGY</a><a href="#" class="active">VALOMIR ENGINEERING</a>
      <a href="#" class="btn btn-orange">CONTACT</a>
    </div>
  </nav>
  <div class="hero-copy">
    <h1 class="display">Engineering Precision.<br><span>Built for Performance.</span></h1>
    <p>Valomir Engineering provides consulting and project management services across cooling, ventilation, heating, and energy systems.</p>
    <div class="hero-actions">
      <a href="#" class="btn btn-orange">EXPLORE VALOMIR ENERGY</a>
      <a href="#" class="btn btn-blue">EXPLORE VALOMIR ENGINEERING</a>
    </div>
  </div>
</section>
<div class="seal" style="top:638px"></div>

<section class="expertise">
  <h2 class="display">Specialized Knowledge<br>Across Every System</h2>
  <p class="sub">Our engineering consultants bring hands-on experience in designing and managing complex technical projects.</p>
  <div class="systems">
    <div class="system-card">
      <svg viewBox="0 0 52 52" fill="none" stroke="#f39a1e" stroke-width="2"><path d="M26 6v40M9 16l34 20M9 36l34-20"/><circle cx="26" cy="26" r="5"/></svg>
      <span>Cooling and<br>refrigeration systems</span>
    </div>
    <div class="system-card">
      <svg viewBox="0 0 52 52" fill="none" stroke="#f39a1e" stroke-width="2"><rect x="8" y="8" width="36" height="36" rx="3"/><circle cx="26" cy="26" r="10"/><path d="M26 16v20M16 26h20"/></svg>
      <span>Ventilation and air<br>quality</span>
    </div>
    <div class="system-card">
      <svg viewBox="0 0 52 52" fill="none" stroke="#f39a1e" stroke-width="2"><rect x="8" y="12" width="36" height="28" rx="3"/><path d="M16 12v28M24 12v28M32 12v28M40 12v28"/></svg>
      <span>Heating systems</span>
    </div>
    <div class="system-card">
      <svg viewBox="0 0 52 52" fill="none" stroke="#f39a1e" stroke-width="2"><circle cx="26" cy="26" r="9"/><path d="M26 6v8M26 38v8M6 26h8M38 26h8M12 12l6 6M34 34l6 6M40 12l-6 6M18 34l-6 6"/></svg>
      <span>Energy systems<br>integration</span>
    </div>
  </div>
</section>

<section class="services">
  <div class="services-photo" role="img" aria-label="Engineers in hard hats reviewing equipment on site"></div>
  <div class="services-copy">
    <h2 class="display">Comprehensive<br>Tech Services</h2>
    <ul class="service-list">
      <li>Project planning and design</li>
      <li>Project management</li>
      <li>Technical inspections and audits</li>
      <li>Operational analysis and optimization</li>
      <li>Technical investigations and reports</li>
    </ul>
  </div>
</section>

<section class="band">
  <h2 class="display">Driven by Expertise.<br>Focused on Efficiency.</h2>
  <p>With a blend of technical excellence and client-centered service, we help businesses operate smarter, safer, and more sustainably.</p>
  <a href="#" class="btn btn-blue">CONTACT OUR ENGINEERING TEAM</a>
</section>

<section class="process">
  <h2 class="display">Collaborative.Transparent.<br>Results-Oriented.</h2>
  <p class="sub">Our process ensures clear communication and measurable outcomes at every stage.</p>
  <div class="steps">
    <div class="step">
      <svg viewBox="0 0 190 190"><path d="M95 8a87 87 0 1 1-87 87" fill="none" stroke="#1f5fb8" stroke-width="3"/><circle cx="95" cy="95" r="70" fill="#fff" stroke="#d9dde2" stroke-width="2"/></svg>
      <h3>Assessment</h3><p>Nemo enim ipsam<br>voluptatem quia voluptas</p>
    </div>
    <div class="step">
      <svg viewBox="0 0 190 190"><path d="M95 8a87 87 0 1 1-87 87" fill="none" stroke="#1f5fb8" stroke-width="3"/><circle cx="95" cy="95" r="70" fill="#f39a1e"/></svg>
      <h3>Design</h3><p>Nemo enim ipsam<br>voluptatem quia voluptas</p>
    </div>
    <div class="step">
      <svg viewBox="0 0 190 190"><path d="M95 8a87 87 0 1 1-87 87" fill="none" stroke="#1f5fb8" stroke-width="3"/><circle cx="95" cy="95" r="70" fill="#fff" stroke="#d9dde2" stroke-width="2"/></svg>
      <h3>Execution</h3><p>Nemo enim ipsam<br>voluptatem quia voluptas</p>
    </div>
    <div class="step">
      <svg viewBox="0 0 190 190"><path d="M95 8a87 87 0 1 1-87 87" fill="none" stroke="#1f5fb8" stroke-width="3"/><circle cx="95" cy="95" r="70" fill="#fff" stroke="#d9dde2" stroke-width="2"/></svg>
      <h3>Optimization</h3><p>Nemo enim ipsam<br>voluptatem quia voluptas</p>
    </div>
  </div>
</section>

<section class="cases">
  <h2 class="display">Our Case Studies</h2>
  <span class="arrow" style="left:80px">&laquo;</span>
  <span class="arrow" style="right:80px">&raquo;</span>
  <div class="case-row">
    <div class="case">
      <div class="case-photo" role="img" aria-label="Technician servicing rooftop HVAC units"></div>
      <h3>HVAC Optimization for ABC Mall</h3>
      <p>Lorem ipsum dolor sit amet, consectetur<br>adipiscing elit, sed do eiusmod tempor.</p>
      <a href="#">VIEW MORE</a>
    </div>
    <div class="case">
      <div class="case-photo" role="img" aria-label="Engineer inspecting a building under construction"></div>
      <h3>HVAC Optimization for ABC Mall</h3>
      <p>Lorem ipsum dolor sit amet, consectetur<br>adipiscing elit, sed do eiusmod tempor.</p>
      <a href="#">VIEW MORE</a>
    </div>
    <div class="case">
      <div class="case-photo" role="img" aria-label="Glass commercial tower against the sky"></div>
      <h3>HVAC Optimization for ABC Mall</h3>
      <p>Lorem ipsum dolor sit amet, consectetur<br>adipiscing elit, sed do eiusmod tempor.</p>
      <a href="#">VIEW MORE</a>
    </div>
  </div>
</section>

<footer class="footer">
  <div class="brand">VALOMIR</div>
  <div class="footer-menu">
    <a href="#">HOME</a><a href="#">ABOUT US</a><a href="#">SERVICES</a><a href="#">VALOMIR ENERGY</a><a href="#">VALOMIR ENGINEERING</a><a href="#">CONTACT US</a>
  </div>
  <div class="footer-rule"></div>
  <div class="contact" style="left:140px"><h4>Email Address</h4>hello@valomir-eng.com</div>
  <div class="contact" style="left:440px"><h4>Phone Number</h4>+1 (555) 014 2290</div>
  <div class="contact" style="left:740px"><h4>Address</h4>48 Harbor Row, Brightwater,<br>USA</div>
  <div class="cert"></div>
  <div class="copyright">Copyright©2025 All Rights Reserved</div>
</footer>
<div class="seal" style="top:3598px"></div>

</body>
</html>
```